Web Design Project

Desisgn a new style for the proposed website as per the attached link. The logo will remain as is, and it is likely that the colours will be as per the attached style guide.

Otherwise look and feel, icons, layout, images are within scope.

Current prosposed home page:
http://marvento-newsite.siteplanrix.example/index

Target Market(s)

Typically, large organisations from any industry such as Airlines, banks, Govt agencies.

Could be operational executives, business improvement specialists, bsuienss analysts.

```html
<!DOCTYPE html>
<html lang="en">
<head>
<meta charset="utf-8">
<title>Marvento – Home</title>
<link rel="stylesheet" href="https://fonts.googleapis.com/css2?family=Roboto+Condensed:wght@300;400;700&family=Noto+Sans:wght@400;700&family=Raleway:wght@400&display=swap">
<style>
  :root {
    --navy: #0b3f8f;
    --navy-dark: #08306f;
    --nav-top: #1a5fb0;
    --nav-bottom: #0a3f86;
    --brand-blue: #1e5ea8;
    --headline-blue: #2173c2;
    --label-blue: #2063ab;
    --green: #6db234;
    --green-dark: #549a20;
    --icon-green: #7bbb35;
    --ink: #333a40;
    --pale: #eaf4fb;
    --line: #cfdde8;
    --footer-text: #e6effa;
    --field: #2b72c4;
  }
  * { box-sizing: border-box; margin: 0; padding: 0; }
  html, body { width: 1200px; height: 929px; overflow: hidden; background: #fff; }
  .stage {
    position: relative; width: 1163px; height: 900px;
    transform: scale(1.0318, 1.0322); transform-origin: 0 0;
    font-family: "Noto Sans", Verdana, sans-serif; color: var(--ink);
  }
  .abs { position: absolute; }

  .color-strip { left: 0; top: 0; width: 1163px; height: 3px;
    background: linear-gradient(90deg, #f39a1e 0 11%, #f5d21a 11% 22%, #6cbf3c 22% 33%, #2bb3e3 33% 44%, #7a4aa5 44% 55%, #e84a8a 55% 66%, #f49ac0 66% 77%, #f39a1e 77% 100%); }
  .header-bg { left: 0; top: 3px; width: 1163px; height: 90px; background: linear-gradient(#e9f3fa, #fff); }

  .brand { left: 183px; top: 15px; display: flex; align-items: center; gap: 12px; }
  .brand-dot { width: 54px; height: 54px; border-radius: 50%; background: #2a8fd3; }
  .brand-name { font-family: "Raleway", sans-serif; font-size: 31px; color: var(--brand-blue); letter-spacing: 0.5px; }

  .main-nav { left: 166px; top: 97px; width: 831px; height: 37px; border-radius: 5px;
    background: linear-gradient(var(--nav-top), var(--nav-bottom)); }
  .main-nav a { position: absolute; top: 0; height: 37px; line-height: 39px; transform: translateX(-50%);
    font-family: "Roboto Condensed", sans-serif; font-size: 15px; color: #fff; text-decoration: none; white-space: nowrap; }
  .main-nav a.is-active { top: 4px; height: 33px; line-height: 31px; width: 64px; text-align: center;
    background: linear-gradient(#ffffff, #dbe9f6); color: var(--brand-blue); border-radius: 4px 4px 0 0; }

  .hero-kicker { left: 190px; top: 192px; font-family: "Roboto Condensed", sans-serif; font-weight: 300;
    font-size: 27px; color: var(--brand-blue); letter-spacing: -0.3px; white-space: nowrap; }
  .hero-title { right: 677px; top: 238px; text-align: right; font-family: "Roboto Condensed", sans-serif;
    font-weight: 700; font-size: 25px; line-height: 40px; color: var(--headline-blue); white-space: nowrap; }
  .btn-more { left: 214px; top: 325px; width: 100px; height: 24px; border-radius: 4px;
    background: linear-gradient(#7cc33e, var(--green-dark)); color: #fff; display: flex; align-items: center;
    justify-content: space-between; padding: 0 4px 0 11px; white-space: nowrap; text-decoration: none;
    font-family: "Roboto Condensed", sans-serif; font-size: 12.5px; line-height: 24px; }
  .btn-more svg { width: 16px; height: 16px; flex: none; }

  .hero-photo { left: 527px; top: 147px; width: 470px; height: 224px; border-radius: 3px;
    background: linear-gradient(160deg, #cfe4f6 0%, #7fb1e0 40%, #2f6cae 75%, #1b3f6e 100%);
    box-shadow: -14px 14px 18px rgba(0,0,0,0.22); }

  .service-box { left: 167px; top: 421px; width: 415px; height: 189px; border: 1px solid var(--line); border-radius: 6px; }
  .service { position: absolute; top: 14px; width: 102px; }
  .service svg.doc { display: block; margin: 0 auto; width: 69px; height: 84px; }
  .service-label { position: relative; margin-top: 15px; height: 58px; border: 1px solid var(--line); border-radius: 6px;
    background: var(--pale); text-align: center; font-family: "Roboto Condensed", sans-serif; font-size: 14px;
    line-height: 20px; padding-top: 8px; color: var(--label-blue); white-space: nowrap; }
  .service-label::before { content: ""; position: absolute; left: 50%; top: -9px; margin-left: -8px;
    border: 8px solid transparent; border-top: 0; border-bottom: 9px solid #dfecf7; }
  .slider-arrow { position: absolute; top: 179px; width: 19px; height: 19px; }

  .benefits { left: 609px; top: 423px; width: 380px; list-style: none; }
  .benefits li { position: relative; padding-left: 26px; font-size: 11px; line-height: 15px; height: 40px; letter-spacing: 0.3px; }
  .benefits svg { position: absolute; left: 0; top: 3px; width: 17px; height: 15px; }

  .footer { left: 0; top: 653px; width: 1163px; height: 247px;
    background: radial-gradient(ellipse 420px 230px at 581px 200px, #2f83d2 0%, #1457aa 45%, var(--navy) 100%); }
  .footer-bar { left: 0; top: 866px; width: 1163px; height: 34px; background: var(--navy-dark); }
  .footer h3 { position: absolute; top: 7px; font-family: "Roboto Condensed", sans-serif; font-weight: 400; font-size: 17px; color: #fff; white-space: nowrap; }
  .footer ul { position: absolute; top: 46px; list-style: none; }
  .footer li { font-size: 11px; line-height: 18.3px; color: var(--footer-text); letter-spacing: 0.4px; white-space: nowrap; }
  .event { position: absolute; left: 183px; font-size: 11px; line-height: 15px; color: var(--footer-text); letter-spacing: 0.3px; white-space: nowrap; }
  .event strong { display: block; color: #bcd6f2; }
  .btn-footer { position: absolute; height: 21px; border-radius: 3px; background: linear-gradient(#7fb8ea, #3d82cc);
    border: 1px solid #9cc7ef; color: #fff; font-family: "Roboto Condensed", sans-serif; font-size: 13px;
    text-align: center; line-height: 19px; white-space: nowrap; }
  .field { position: absolute; left: 802px; width: 180px; border-radius: 4px; background: var(--field);
    border: 1px solid #3a86d6; color: #c6ddf4; font-size: 11px; padding: 4px 8px; letter-spacing: 0.4px; white-space: nowrap; }
  .footer-dot { left: 550px; top: 829px; width: 63px; height: 63px; border-radius: 50%; background: #fff;
    box-shadow: 0 0 14px rgba(120,190,255,0.9); }
  .copyright { left: 169px; top: 877px; font-family: "Roboto Condensed", sans-serif; font-size: 12px; color: #fff; white-space: nowrap; }
  .legal { right: 167px; top: 878px; font-family: "Roboto Condensed", sans-serif; font-size: 10.5px; color: #cfe0f4; white-space: nowrap; }
  .legal span { margin: 0 4px; }
</style>
</head>
<body>
<div class="stage">
  <div class="abs color-strip"></div>
  <div class="abs header-bg"></div>

  <div class="abs brand"><span class="brand-dot"></span><span class="brand-name">marvento</span></div>

  <nav class="abs main-nav">
    <a class="is-active" href="#" style="left:47px">Home</a>
    <a href="#" style="left:137px">About Us</a>
    <a href="#" style="left:236px">Products</a>
    <a href="#" style="left:334px">Services</a>
    <a href="#" style="left:429px">Solution</a>
    <a href="#" style="left:530px">Resources</a>
    <a href="#" style="left:657px">Customer Stories</a>
    <a href="#" style="left:775px">Contact</a>
  </nav>

  <div class="abs hero-kicker">CONTINUOUS IMPROVEMENT</div>
  <div class="abs hero-title">A NATURAL PART OF YOUR<br>BUSINESS PROCESSES</div>
  <a class="abs btn-more" href="#"><span>READ MORE</span>
    <svg viewBox="0 0 16 16"><circle cx="8" cy="8" r="8" fill="#fff"/><path d="M6 4.5 L11.5 8 L6 11.5Z" fill="#4f8f20"/></svg>
  </a>
  <div class="abs hero-photo" role="img" aria-label="Businessman in a suit launching a paper plane against a blue sky between glass office towers"></div>

  <div class="abs service-box">
    <div class="service" style="left:14px">
      <svg class="doc" viewBox="0 0 69 84"><path d="M6 2h42l19 19v57a4 4 0 0 1-4 4H6a4 4 0 0 1-4-4V6a4 4 0 0 1 4-4z" fill="#fff" stroke="var(--icon-green)" stroke-width="3"/><path d="M48 2v19h19" fill="none" stroke="var(--icon-green)" stroke-width="3"/>
        <path d="M10 40h14l4 4h28v24H10z" fill="#222"/><path d="M26 28h18l6 6v14H26z" fill="#fff" stroke="#222" stroke-width="2"/><path d="M8 50h50l-4 18H10z" fill="#333"/></svg>
      <div class="service-label">KNOWLEDGE<br>MANAGEMENT</div>
    </div>
    <div class="service" style="left:156px">
      <svg class="doc" viewBox="0 0 69 84"><path d="M6 2h42l19 19v57a4 4 0 0 1-4 4H6a4 4 0 0 1-4-4V6a4 4 0 0 1 4-4z" fill="#fff" stroke="var(--icon-green)" stroke-width="3"/><path d="M48 2v19h19" fill="none" stroke="var(--icon-green)" stroke-width="3"/>
        <path d="M10 36v24h50" fill="none" stroke="#222" stroke-width="2"/><rect x="14" y="50" width="5" height="9" fill="#222"/><rect x="22" y="46" width="5" height="13" fill="#222"/><rect x="30" y="48" width="5" height="11" fill="#222"/><rect x="38" y="42" width="5" height="17" fill="#222"/><rect x="46" y="38" width="5" height="21" fill="#222"/><path d="M12 46l10-8 8 5 14-12" fill="none" stroke="#222" stroke-width="2"/><path d="M40 29h7v7" fill="none" stroke="#222" stroke-width="2"/></svg>
      <div class="service-label">CONTINUOUS<br>IMPROVEMENT</div>
    </div>
    <div class="service" style="left:299px">
      <svg class="doc" viewBox="0 0 69 84"><path d="M6 2h42l19 19v57a4 4 0 0 1-4 4H6a4 4 0 0 1-4-4V6a4 4 0 0 1 4-4z" fill="#fff" stroke="var(--icon-green)" stroke-width="3"/><path d="M48 2v19h19" fill="none" stroke="var(--icon-green)" stroke-width="3"/>
        <path d="M25 37a14 14 0 1 0 18 0" fill="none" stroke="#222" stroke-width="5" stroke-linecap="round"/><path d="M34 28v17" stroke="#222" stroke-width="5" stroke-linecap="round"/></svg>
      <div class="service-label">SYSTEM<br>REQUIREMENTS</div>
    </div>
    <svg class="slider-arrow" style="left:29px" viewBox="0 0 19 19"><circle cx="9.5" cy="9.5" r="8.5" fill="#e4e6e8" stroke="#b8bcc0"/><path d="M11.5 5.5L7 9.5l4.5 4" fill="none" stroke="#7d8389" stroke-width="2"/></svg>
    <svg class="slider-arrow" style="left:367px" viewBox="0 0 19 19"><circle cx="9.5" cy="9.5" r="8.5" fill="#e4e6e8" stroke="#b8bcc0"/><path d="M7.5 5.5L12 9.5l-4.5 4" fill="none" stroke="#7d8389" stroke-width="2"/></svg>
  </div>

  <ul class="abs benefits">
    <li><svg viewBox="0 0 17 15"><path d="M1 8l5 5L16 2" fill="none" stroke="var(--green)" stroke-width="3"/></svg>Build a knowledge management system that captures and reuses your expertise.</li>
    <li><svg viewBox="0 0 17 15"><path d="M1 8l5 5L16 2" fill="none" stroke="var(--green)" stroke-width="3"/></svg>Undertake business transformations that reduce risk and cost and increase the benefits.</li>
    <li><svg viewBox="0 0 17 15"><path d="M1 8l5 5L16 2" fill="none" stroke="var(--green)" stroke-width="3"/></svg>Implement continuous improvement as a natural part of your business processes.</li>
    <li><svg viewBox="0 0 17 15"><path d="M1 8l5 5L16 2" fill="none" stroke="var(--green)" stroke-width="3"/></svg>Create business process models that are understood to business users.</li>
    <li><svg viewBox="0 0 17 15"><path d="M1 8l5 5L16 2" fill="none" stroke="var(--green)" stroke-width="3"/></svg>Create systems requirements that relate business processes to IT systems capability.</li>
  </ul>

  <footer class="abs footer">
    <h3 style="left:183px">News &amp; Events</h3>
    <h3 style="left:381px">Products</h3>
    <h3 style="left:626px">Training &amp; Support</h3>
    <h3 style="left:803px">Quick Contact</h3>

    <div class="event" style="top:49px"><strong>Sydney</strong>Elements of Improvement</div>
    <div class="event" style="top:91px"><strong>Melbourne</strong>BPI &amp; Business Process</div>
    <div class="btn-footer" style="left:183px;top:134px;width:72px">Read more</div>

    <ul style="left:382px">
      <li>Processbase</li><li>Marvento Modeler</li><li>System Requirements Modeler</li>
      <li>Performance Improvement Modeler</li><li>Enterprise Architect Modeler</li><li>Corporate Governance Modeler</li>
    </ul>
    <ul style="left:626px">
      <li>Text-Based Tutorials</li><li>Tutorial Movies</li><li>Knowledge Base</li><li>Forums</li><li>Training Courses</li>
    </ul>

    <div class="field" style="top:47px;height:23px">Enter your name</div>
    <div class="field" style="top:77px;height:23px">Enter your email</div>
    <div class="field" style="top:107px;height:56px">Discription</div>
    <div class="btn-footer" style="left:856px;top:171px;width:72px">Submit</div>
  </footer>
  <div class="abs footer-bar"></div>
  <div class="abs footer-dot"></div>
  <div class="abs copyright">© Copyright MARVENTO 2012 - All Rights Reserved</div>
  <div class="abs legal">TERMS &amp; CONDITIONS<span>|</span>PRIVACY POLICY<span>|</span>MAINTENANCE POLICY</div>
</div>
</body>
</html>
```